Corvelle Strategies business card

I need a business card for my new strategic consulting LLC, Corvelle Strategies. We specialize in helping people who care about broadband technology and telecommunications policy, and we're based in Washington DC. I'm looking for a card that says smart, credible, future-facing and signals a high level of expertise. It's DC, so there's clearly a limit to how crazy we can go with this card, but I am looking for a design that reflects a company that is comfortable with technology, policy, and having a little bit fun. I'm uploading my logo below, and I'd like to have it be part of the card design in some fashion.
Target Market(s)
Telecommunications and technology policy professionals
Industry/Entity Type
Technology policy
Contact Information for Business Card
Name of business, my name (Glen Mosswater), email (glen@corvellestrategies-example.com) , phone number (202-555-0148)phone number

```html
<!DOCTYPE html>
<html lang="en">
<head>
<meta charset="utf-8">
<title>Corvelle Strategies — Business Card</title>
<link rel="stylesheet" href="https://fonts.googleapis.com/css2?family=EB+Garamond:wght@400;700&display=swap">
<style>
  :root {
    --stage: #e9e6e1;
    --navy-deep: #0a2a66;
    --navy: #0d3a80;
    --royal: #0f4fa8;
    --gold: #f0a93b;
    --white: #ffffff;
    --paper: #f3f3f3;
    --ink-light: #e6ecf7;
  }
  * { box-sizing: border-box; margin: 0; padding: 0; }
  html, body {
    width: 1200px; height: 900px; overflow: hidden;
    background: var(--stage);
    font-family: "EB Garamond", Georgia, serif;
  }
  .stage { position: relative; width: 1200px; height: 900px; }

  .card {
    position: absolute;
    width: 600px; height: 343px;
    border-radius: 46px 0 46px 0;
    overflow: hidden;
    box-shadow: 0 14px 30px rgba(0,0,0,.22);
  }

  /* Back of card */
  .card--back {
    left: 300px; top: 70px;
    background: linear-gradient(135deg, var(--royal) 0%, var(--navy) 55%, var(--navy-deep) 100%);
  }
  .card--back .wordmark {
    position: absolute; right: 48px; top: 56px;
    color: var(--white);
    font-size: 44px; font-weight: 700; line-height: 1;
    display: flex; align-items: center; gap: 12px;
  }
  .card--back .decor-field {
    position: absolute; left: 60px; bottom: 0;
    width: 300px; height: 250px;
    border-radius: 40px 40px 0 0;
    background: linear-gradient(160deg, rgba(10,42,102,.35), rgba(15,79,168,.15));
  }

  /* Front of card */
  .card--front {
    left: 300px; top: 480px;
    background: linear-gradient(160deg, var(--white) 40%, var(--paper) 100%);
  }
  .card--front .panel { position: absolute; inset: 0; width: 100%; height: 100%; }
  .contact {
    position: absolute; left: 36px; top: 96px;
    color: var(--ink-light);
  }
  .contact__name {
    color: var(--gold);
    font-size: 22px; font-weight: 700; letter-spacing: .5px;
    line-height: 1.2;
    text-transform: uppercase;
  }
  .contact__rule {
    width: 110px; height: 1px; background: var(--gold);
    margin: 8px 0 12px;
  }
  .contact__line {
    display: flex; align-items: center; gap: 9px;
    font-size: 15px; line-height: 1.6; white-space: nowrap;
  }
  .contact__line svg { width: 14px; height: 14px; flex: none; }

  .art-field {
    position: absolute; right: 20px; top: 16px;
    width: 200px; height: 130px;
    border-radius: 6px;
    background: linear-gradient(180deg, rgba(15,79,168,.16), rgba(15,79,168,.05));
  }
  .card--front .wordmark {
    position: absolute; right: 30px; bottom: 34px;
    color: var(--royal);
    font-size: 30px; font-weight: 700; line-height: 1;
    display: flex; align-items: center; gap: 9px;
    white-space: nowrap;
  }
  .dot { display: inline-block; border-radius: 50%; background: var(--gold); }
  .card--back .dot { width: 30px; height: 30px; }
  .card--front .dot { width: 18px; height: 18px; }
</style>
</head>
<body>
<main class="stage">

  <section class="card card--back" aria-label="Card back">
    <div class="decor-field" role="img" aria-label="Faint embossed brand emblem area"></div>
    <div class="wordmark"><span class="dot"></span>Corvelle Strategies</div>
  </section>

  <section class="card card--front" aria-label="Card front">
    <svg class="panel" viewBox="0 0 600 343" preserveAspectRatio="none" aria-hidden="true">
      <polygon points="0,0 560,0 170,343 0,343" fill="var(--navy-deep)"/>
      <polygon points="560,0 590,0 190,343 170,343" fill="var(--white)"/>
      <polygon points="590,0 625,0 225,343 190,343" fill="var(--royal)"/>
    </svg>

    <div class="art-field" role="img" aria-label="Brand emblem area"></div>

    <div class="contact">
      <p class="contact__name">Glen Mosswater</p>
      <div class="contact__rule"></div>
      <p class="contact__line">
        <svg viewBox="0 0 24 24" aria-hidden="true"><path fill="var(--gold)" d="M6.6 10.8a15.2 15.2 0 0 0 6.6 6.6l2.2-2.2a1 1 0 0 1 1-.25 11.4 11.4 0 0 0 3.6.57 1 1 0 0 1 1 1V20a1 1 0 0 1-1 1A17 17 0 0 1 3 4a1 1 0 0 1 1-1h3.5a1 1 0 0 1 1 1c0 1.25.2 2.45.57 3.6a1 1 0 0 1-.25 1z"/></svg>
        202-555-0148
      </p>
      <p class="contact__line">
        <svg viewBox="0 0 24 24" aria-hidden="true"><path fill="var(--gold)" d="M2 5h20v14H2z M3.5 6.5 12 13l8.5-6.5" stroke="var(--navy-deep)" stroke-width="1.4"/></svg>
        glen@corvellestrategies-example.com
      </p>
    </div>

    <div class="wordmark"><span class="dot"></span>Corvelle Strategies</div>
  </section>

</main>
</body>
</html>
```